Stationary for a property rental company
Glenbrook Rentals
Stationary for a property rental company - Real Estate
Creative Brief
Simple
Marla Pike
Owner
PO Box 7413 Ashford Falls, VT 05199
marla@glenbrookrentals-example.net
www.glenbrookrentals-example.net
Please use similar colors that are found in the Logo.
Use emblem for the back of the card

```html
<!DOCTYPE html>
<html lang="en">
<head>
<meta charset="utf-8">
<title>Glenbrook Rentals – Business Card</title>
<link rel="stylesheet" href="https://fonts.googleapis.com/css2?family=Cormorant+Garamond:wght@600&family=Lato:wght@400;700&display=swap">
<style>
  :root {
    --stage: #ecedef;
    --card-white: #ffffff;
    --brand-blue: #5e9cc6;
    --brand-blue-light: #7db2d6;
    --navy: #2f4a6b;
    --text-blue: #4d87b4;
    --text-grey: #6f7780;
    --rule: #c9d4de;
  }
  * { margin: 0; padding: 0; box-sizing: border-box; }
  html, body { width: 1200px; height: 629px; overflow: hidden; }
  body {
    background: var(--stage);
    display: flex;
    align-items: center;
    justify-content: center;
    gap: 60px;
    font-family: "Lato", sans-serif;
  }
  .card {
    width: 500px;
    height: 286px;
    border-radius: 4px;
    box-shadow: 0 6px 18px rgba(0,0,0,0.12);
    position: relative;
    overflow: hidden;
  }
  .card-back {
    background: radial-gradient(circle at 50% 45%, var(--brand-blue-light), var(--brand-blue) 75%);
    display: flex;
    align-items: center;
    justify-content: center;
  }
  .card-front {
    background: var(--card-white);
    display: flex;
    align-items: center;
    padding: 0 34px;
  }
  .brand {
    display: flex;
    flex-direction: column;
    align-items: center;
    gap: 10px;
  }
  .brand-dot {
    width: 46px;
    height: 46px;
    border-radius: 50%;
    background: var(--navy);
  }
  .card-back .brand-dot { background: var(--card-white); }
  .brand-name {
    font-family: "Cormorant Garamond", serif;
    font-weight: 600;
    font-size: 26px;
    letter-spacing: 1.5px;
    text-transform: uppercase;
    color: var(--navy);
    text-align: center;
    line-height: 1.05;
  }
  .card-back .brand-name { color: var(--card-white); font-size: 28px; }
  .card-front .brand { width: 180px; }
  .divider {
    width: 1px;
    height: 170px;
    background: var(--rule);
    margin: 0 24px 0 20px;
  }
  .contact { display: flex; flex-direction: column; }
  .person-name {
    font-family: "Cormorant Garamond", serif;
    font-weight: 600;
    font-size: 19px;
    color: var(--text-blue);
    letter-spacing: 0.5px;
  }
  .person-title {
    font-size: 10px;
    color: var(--text-grey);
    text-transform: uppercase;
    letter-spacing: 1.5px;
    margin: 2px 0 16px;
  }
  .contact-list { list-style: none; display: flex; flex-direction: column; gap: 7px; }
  .contact-item {
    display: flex;
    align-items: flex-start;
    gap: 8px;
    font-size: 10px;
    color: var(--text-grey);
    line-height: 1.35;
  }
  .contact-icon { width: 12px; height: 12px; flex: none; margin-top: 1px; }
</style>
</head>
<body>
  <section class="card card-back" aria-label="Card back">
    <div class="brand">
      <span class="brand-dot"></span>
      <span class="brand-name">Glenbrook<br>Rentals</span>
    </div>
  </section>

  <section class="card card-front" aria-label="Card front">
    <div class="brand">
      <span class="brand-dot"></span>
      <span class="brand-name">Glenbrook<br>Rentals</span>
    </div>
    <div class="divider"></div>
    <div class="contact">
      <p class="person-name">Marla Pike</p>
      <p class="person-title">Owner</p>
      <ul class="contact-list">
        <li class="contact-item">
          <svg class="contact-icon" viewBox="0 0 12 12"><circle cx="6" cy="6" r="6" fill="#5e9cc6"/><path d="M6 2.5a2.2 2.2 0 0 0-2.2 2.2C3.8 6.4 6 9.5 6 9.5s2.2-3.1 2.2-4.8A2.2 2.2 0 0 0 6 2.5z" fill="#fff"/></svg>
          <span>PO Box 7413<br>Ashford Falls, VT 05199</span>
        </li>
        <li class="contact-item">
          <svg class="contact-icon" viewBox="0 0 12 12"><circle cx="6" cy="6" r="6" fill="#5e9cc6"/><path d="M4 3h1.3l.6 1.5-.8.6a4.5 4.5 0 0 0 1.8 1.8l.6-.8L9 6.7V8a1 1 0 0 1-1 1A5 5 0 0 1 3 4a1 1 0 0 1 1-1z" fill="#fff"/></svg>
          <span>802-555-0147</span>
        </li>
        <li class="contact-item">
          <svg class="contact-icon" viewBox="0 0 12 12"><circle cx="6" cy="6" r="6" fill="#5e9cc6"/><rect x="3" y="4" width="6" height="4.2" fill="#fff"/><path d="M3 4l3 2.3L9 4" stroke="#5e9cc6" stroke-width="0.7" fill="none"/></svg>
          <span>marla@glenbrookrentals-example.net</span>
        </li>
        <li class="contact-item">
          <svg class="contact-icon" viewBox="0 0 12 12"><circle cx="6" cy="6" r="6" fill="#5e9cc6"/><circle cx="6" cy="6" r="3" stroke="#fff" stroke-width="0.8" fill="none"/><path d="M3 6h6M6 3c-1.2 1.6-1.2 4.4 0 6M6 3c1.2 1.6 1.2 4.4 0 6" stroke="#fff" stroke-width="0.6" fill="none"/></svg>
          <span>www.glenbrookrentals-example.net</span>
        </li>
      </ul>
    </div>
  </section>
</body>
</html>
```